Stationary - Business Card/Letterhead and envelope design

Details for my new Stationery Design Project will be added soon. , I have two logos I am trying to decide on. I will upload the eps logos shortly. I have attached a file of what i have so far. I need urgently Business cards, but also will need a letterhead template and envelopes.

PLEASE NOTE THE DEADLINE SAYS 2 DAYS but I need business card design in LESS THAN A DAY.

thanks, Details for my new Stationery Design Project will be added soon. , I have two logos I am trying to decide on. I will upload the eps logos shortly. I have attached a file of what i have so far. I need urgently Business cards, but also will need a letterhead template and envelopes.

thanks
Updates

I have uploaded one of the logos you can work with. hopefully the other one comes soon.

details for the business card.

Marla Thorne

Managing Director

P&K Ventures Ltd

Bda: 1-441-555-0193

Email: marla@pkvnbda.com

web: www.pkvnbda.com

Industry/Entity Type

Business

```html
<!DOCTYPE html>
<html lang="en">
<head>
<meta charset="utf-8">
<title>P&amp;K Ventures – Business Card</title>
<link href="https://fonts.googleapis.com/css2?family=Lato:wght@400;700;900&display=swap" rel="stylesheet">
<style>
  :root{
    --stage:#1c140f;
    --card-dark:#1b1b1d;
    --card-dark-edge:#0c0c0d;
    --card-light:#ffffff;
    --frame-light:#d9d9d9;
    --frame-blue:#2a6fc0;
    --brand-blue:#2a78cc;
    --accent-green:#6cb33f;
    --ink:#161616;
    --ink-soft:#333333;
    --ink-muted:#555555;
  }
  *{box-sizing:border-box;margin:0;padding:0}
  html,body{width:1200px;height:2257px;overflow:hidden;background:var(--stage)}
  body{font-family:"Lato",Arial,sans-serif}
  .sheet{position:relative;width:1200px;height:2257px}
  .row{position:absolute;left:0;width:1200px;height:752px}
  .row--front{top:0}
  .row--back{top:752px}
  .row--front-light{top:1504px}
  .card{position:absolute;left:150px;top:119px;width:900px;height:514px;border-radius:10px;overflow:hidden;box-shadow:0 18px 40px rgba(0,0,0,.55)}
  .card--dark{background:radial-gradient(ellipse at 50% 40%,#3a3a3d 0%,var(--card-dark) 55%,var(--card-dark-edge) 100%)}
  .card--light{background:var(--card-light)}
  .card__frame{position:absolute;inset:0;width:900px;height:514px}
  .brand{position:absolute;inset:0;display:flex;align-items:center;justify-content:center;gap:18px}
  .brand__mark{width:30px;height:30px;background:var(--accent-green);flex:none}
  .brand__name{font-weight:900;font-size:56px;letter-spacing:2px;color:var(--brand-blue);text-transform:uppercase;white-space:nowrap}
  /* back */
  .back__side{position:absolute;left:0;top:0;width:380px;height:514px;background:radial-gradient(ellipse at 40% 45%,#333336 0%,var(--card-dark) 60%,var(--card-dark-edge) 100%)}
  .back__side .brand{gap:12px;padding-right:20px}
  .back__side .brand__name{font-size:34px}
  .back__side .brand__mark{width:20px;height:20px}
  .back__panel{position:absolute;left:330px;top:0;width:570px;height:514px}
  .panel-shape{position:absolute;inset:0;width:570px;height:514px}
  .contact{position:absolute;left:90px;top:118px;color:var(--ink)}
  .contact__name{font-weight:900;font-size:44px;text-transform:uppercase;letter-spacing:-.5px;line-height:1.1}
  .contact__role{font-size:20px;color:var(--ink-muted);margin:8px 0 26px}
  .contact__list{list-style:none}
  .contact__item{display:flex;align-items:center;gap:14px;font-size:22px;line-height:1.75;color:var(--ink-soft)}
  .contact__icon{width:20px;height:20px;flex:none}
</style>
</head>
<body>
<main class="sheet">

  <section class="row row--front" aria-label="Card front, dark">
    <div class="card card--dark">
      <svg class="card__frame" viewBox="0 0 900 514" aria-hidden="true">
        <path d="M66,30 H834 Q870,30 870,66 V300 L855,315 L870,330 V448 Q870,484 834,484 H66 Q30,484 30,448 V180 L45,165 L30,150 V66 Q30,30 66,30 Z" fill="none" stroke="var(--frame-light)" stroke-width="3"/>
        <path d="M22,150 L37,165 L22,180" fill="none" stroke="var(--accent-green)" stroke-width="3"/>
        <path d="M878,300 L863,315 L878,330" fill="none" stroke="var(--accent-green)" stroke-width="3"/>
      </svg>
      <div class="brand"><span class="brand__mark"></span><span class="brand__name">P&amp;K Ventures</span></div>
    </div>
  </section>

  <section class="row row--back" aria-label="Card back">
    <div class="card card--light">
      <div class="back__side">
        <div class="brand"><span class="brand__mark"></span><span class="brand__name">P&amp;K Ventures</span></div>
      </div>
      <div class="back__panel">
        <svg class="panel-shape" viewBox="0 0 570 514" aria-hidden="true">
          <path d="M50,0 H570 V514 H50 V250 L0,225 L50,200 Z" fill="var(--card-light)"/>
        </svg>
        <div class="contact">
          <p class="contact__name">Marla Thorne</p>
          <p class="contact__role">Managing Director</p>
          <ul class="contact__list">
            <li class="contact__item">
              <svg class="contact__icon" viewBox="0 0 20 20" aria-hidden="true"><rect x="1" y="4" width="18" height="12" fill="#333"/><path d="M1,4 L10,11 L19,4" fill="none" stroke="#fff" stroke-width="1.5"/></svg>
              marla@pkvnbda.com</li>
            <li class="contact__item">
              <svg class="contact__icon" viewBox="0 0 20 20" aria-hidden="true"><rect x="5" y="1" width="10" height="18" rx="2" fill="none" stroke="#333" stroke-width="2"/><circle cx="10" cy="15.5" r="1.2" fill="#333"/></svg>
              1-441-555-0193</li>
            <li class="contact__item">
              <svg class="contact__icon" viewBox="0 0 20 20" aria-hidden="true"><path d="M10,1 C6,1 4,4 4,7 C4,12 10,19 10,19 C10,19 16,12 16,7 C16,4 14,1 10,1 Z" fill="#333"/><circle cx="10" cy="7" r="2.2" fill="#fff"/></svg>
              18 Harbour Lane Suite 4B</li>
            <li class="contact__item">
              <svg class="contact__icon" viewBox="0 0 20 20" aria-hidden="true"><circle cx="10" cy="10" r="8" fill="none" stroke="#333" stroke-width="1.8"/><ellipse cx="10" cy="10" rx="3.5" ry="8" fill="none" stroke="#333" stroke-width="1.4"/><path d="M2,10 H18" stroke="#333" stroke-width="1.4"/></svg>
              www.pkvnbda.com</li>
          </ul>
        </div>
      </div>
    </div>
  </section>

  <section class="row row--front-light" aria-label="Card front, light">
    <div class="card card--light">
      <svg class="card__frame" viewBox="0 0 900 514" aria-hidden="true">
        <path d="M66,30 H834 Q870,30 870,66 V300 L855,315 L870,330 V448 Q870,484 834,484 H66 Q30,484 30,448 V180 L45,165 L30,150 V66 Q30,30 66,30 Z" fill="none" stroke="var(--frame-blue)" stroke-width="3"/>
        <path d="M22,150 L37,165 L22,180" fill="none" stroke="var(--accent-green)" stroke-width="3"/>
        <path d="M878,300 L863,315 L878,330" fill="none" stroke="var(--accent-green)" stroke-width="3"/>
      </svg>
      <div class="brand"><span class="brand__mark"></span><span class="brand__name">P&amp;K Ventures</span></div>
    </div>
  </section>

</main>
</body>
</html>
```